依頼詳細
演目「ミルフォーネ」。古典バレエの演目で、幼児から大人まで出演いたします。
従来のイメージにこだわりません。添付画像を加工してご使用いただけると幸いです。必ず3人が使用されていることが希望です。かわいいもの、劇画調のもの、クールでシャープなドラマチックな感じのものなど、何でも幅広くお力をお借りできればと思います。
よろしくお願いいたします。
記載項目
主催:ルミエダンス お問合せ先:ルミエダンス事務局 0598-41-6273
サイズ
A4
ページ数
片面
希望イメージ
シンプル 複雑
単色 カラフル
暗い 明るい
日常 高級
遊び心 厳粛
未来的 伝統的
女性的 男性的
希望する色
納品ファイル
• 高解像度JPG (.jpg)
• イラストレーター形式 (.ai)
補足説明
お世話になります。
いろいろなご提案をいただき、ありがとうございます。

ミルフォーネという演目は、イメージがとってもあまり観られる機会もなく、イメージが難しいかと思います。
良い画像ではありませんが、ダンサーを漫画風、劇画調、モノクロ、などに加工していただいたりするものも良いのではないか、という意見も内部でございます。

どうぞお力をお貸しいただけるとうれしいです。
よろしくお願いいたします。
■ 選んだ理由

お世話になっております。
何より鮮やかなレッドのインパクトとバランスの良く大胆な構成に惹かれました。

■ 提案者全員のお礼・コメント

お世話になっております。
この度は多くのご提案をいただき本当にありがとうございました。
どの作品もすばらしく、スタッフ内で票も割れてとても悩みました。
また、機会がございましたらお力を拝借できるとたいへんうれしいです。
ありがとうございました。

```html
<!DOCTYPE html>
<html lang="ja">
<head>
<meta charset="utf-8">
<title>ルミエダンス 発表会公演 ミルフォーネ</title>
<link href="https://fonts.googleapis.com/css2?family=Great+Vibes&family=Noto+Sans+JP:wght@400;700&family=Noto+Serif+JP:wght@500;700;900&display=swap" rel="stylesheet">
<style>
:root{
  --night:#17121c;
  --night-deep:#0b080e;
  --pink:#f48fb8;
  --pink-soft:#f9c4da;
  --gold:#d9a93c;
  --gold-light:#f7dd8a;
  --gold-dark:#8a5d17;
  --white:#ffffff;
  --grey:#bdb6c4;
}
*{margin:0;padding:0;box-sizing:border-box}
html,body{width:875px;height:1200px;overflow:hidden;background:var(--night-deep)}
.poster{
  position:relative;width:875px;height:1200px;overflow:hidden;
  font-family:"Noto Serif JP",serif;color:var(--white);
  background:
    radial-gradient(circle at 72% 38%,rgba(255,220,120,.35),transparent 30%),
    radial-gradient(circle at 90% 15%,rgba(120,200,255,.25),transparent 22%),
    radial-gradient(circle at 15% 55%,rgba(255,120,180,.22),transparent 25%),
    radial-gradient(circle at 60% 70%,rgba(140,255,180,.18),transparent 25%),
    linear-gradient(180deg,var(--night) 0%,#221a26 55%,var(--night-deep) 100%);
}
.brand-top{position:absolute;top:30px;left:0;width:100%;text-align:center}
.brand-top .name{font-size:46px;font-weight:700;color:var(--pink);letter-spacing:4px}
.brand-top .event{font-size:22px;margin-left:10px;letter-spacing:3px}
.ribbon{position:absolute;top:100px;left:95px;width:700px;height:150px}
.title{position:absolute;top:118px;left:0;width:100%;text-align:center}
.title .ja{font-size:18px;color:var(--gold-dark);font-weight:700;letter-spacing:4px;display:block;margin-left:150px}
.title .en{font-family:"Great Vibes",cursive;font-size:80px;color:var(--white);line-height:1;text-shadow:0 0 2px var(--gold-dark)}
.dancers-photo{
  position:absolute;top:235px;left:340px;width:470px;height:460px;border-radius:50% 50% 20px 20px/30% 30% 20px 20px;
  background:radial-gradient(ellipse at 50% 45%,#f4e7ea 0%,#d9b9c2 40%,rgba(150,110,130,.5) 75%,transparent 100%);
}
.schedule{position:absolute;left:55px;top:300px;width:330px}
.show{margin-bottom:30px}
.show .year{font-size:14px;color:var(--pink-soft);display:block}
.show .date{font-size:36px;font-weight:900;color:var(--pink);line-height:1.1}
.show .date small{font-size:20px}
.show .venue{font-size:17px;font-weight:700;margin-top:6px;border-bottom:1px solid var(--grey);padding-bottom:4px}
.show .time{font-size:13px;color:var(--grey);margin-top:4px}
.price{font-size:16px;font-weight:700}
.price span{font-size:13px;color:var(--grey)}
.girl-illustration{
  position:absolute;left:30px;top:700px;width:250px;height:300px;border-radius:50% 50% 40% 40%;
  background:radial-gradient(ellipse at 50% 40%,#fbd3e4 0%,#f29cc0 50%,rgba(244,143,184,.15) 80%,transparent 100%);
}
.brand-main{position:absolute;top:830px;left:280px;width:540px;text-align:center}
.brand-main .name{font-size:76px;font-weight:900;color:var(--pink);letter-spacing:6px}
.brand-main .url{font-family:"Noto Sans JP",sans-serif;font-size:12px;color:var(--pink-soft)}
.contact{position:absolute;top:1000px;left:280px;width:560px;font-family:"Noto Sans JP",sans-serif}
.contact .label{font-size:16px;font-weight:700;color:var(--pink-soft);text-align:center;margin-bottom:10px}
.contact .row{display:flex;align-items:center;gap:10px;margin-bottom:8px}
.contact .office{font-size:14px}
.contact .phone{font-size:32px;font-weight:700;letter-spacing:1px}
.contact .net{font-size:15px;gap:24px}
.icon{width:26px;height:26px;flex:none}
.note{position:absolute;bottom:22px;left:0;width:100%;text-align:center;font-family:"Noto Sans JP",sans-serif;font-size:11px;color:var(--grey)}
</style>
</head>
<body>
<main class="poster">
  <header class="brand-top"><span class="name">ルミエダンス</span><span class="event">発表会公演</span></header>

  <svg class="ribbon" viewBox="0 0 700 150" aria-hidden="true">
    <defs>
      <linearGradient id="goldBand" x1="0" y1="0" x2="0" y2="1">
        <stop offset="0" stop-color="var(--gold-light)"/><stop offset=".5" stop-color="var(--gold)"/><stop offset="1" stop-color="var(--gold-dark)"/>
      </linearGradient>
    </defs>
    <path d="M0 70 L70 60 L70 130 L0 140 L25 105 Z" fill="var(--gold-dark)"/>
    <path d="M700 70 L630 60 L630 130 L700 140 L675 105 Z" fill="var(--gold-dark)"/>
    <path d="M60 40 Q350 -10 640 40 L640 120 Q350 70 60 120 Z" fill="url(#goldBand)"/>
  </svg>
  <h1 class="title"><span class="ja">ミルフォーネ</span><span class="en">Milfone</span></h1>

  <div class="dancers-photo" role="img" aria-label="バレエ衣装の3人のダンサーの写真"></div>

  <section class="schedule">
    <div class="show">
      <span class="year">2020</span>
      <div class="date">3/20<small>(祝・金)</small></div>
      <div class="venue">桜台市民会館　大ホール</div>
      <div class="time">00:00開場 00:00開演</div>
    </div>
    <div class="show">
      <span class="year">2020</span>
      <div class="date">3/28<small>(土)</small>・3/29<small>(日)</small></div>
      <div class="venue">みどり野市民会館　ひかりホール</div>
      <div class="time">00:00開場 00:00開演</div>
    </div>
    <p class="price">前売り 500円 ◆ 当日 1,000円 <span>(全席自由)</span></p>
  </section>

  <div class="girl-illustration" role="img" aria-label="ピンクのドレスの少女のイラスト"></div>

  <div class="brand-main"><div class="name">ルミエダンス</div><div class="url">lumiedance.jp</div></div>

  <section class="contact">
    <div class="label">お問い合わせ</div>
    <div class="row">
      <span class="office">ルミエダンス事務局</span>
      <svg class="icon" viewBox="0 0 24 24" aria-hidden="true"><rect width="24" height="24" rx="4" fill="var(--white)"/><path d="M7 5l3 3-2 2q2 4 6 6l2-2 3 3-2 3Q8 19 4 7z" fill="var(--night)"/></svg>
      <span class="phone">0598-41-6273</span>
    </div>
    <div class="row net">
      <span>✉ info@lumiedance.jp</span>
      <span>● www.lumiedance.jp</span>
    </div>
  </section>

  <p class="note">チケットのお求めは事務局までお問い合わせください。</p>
</main>
</body>
</html>
```